Wexcombe Dance Company needs an A-frame sign design

Wexcombe Dance Company needs an A-frame sign for placing on the street outside of our dance studio. We are a dance school with a difference, offering recreational dance classes in various styles including contemporary, hip hop, ballet, jazz and capoeira as well as performance opportunities. We also are Creative Arts Therapists specialising in Dance Movement Therapy. I would like to see a design that incorporates our logo and lists the services we have, as well as our contact information (phone number and email address). I want the design to be not too busy, is bold and has a professional, clean quality to it, potentially utilising the three colours in our logo design. I'm interested in seeing two designs; one without any images of people and one that incorporates a photo.
Target Market(s)
Families with children, adults interested in dance
Requirements
Must have
- Logo, list all of our dance styles and the text 'Creative Art Therapy - QPHW Registered'

```html
<!DOCTYPE html>
<html lang="en">
<head>
<meta charset="utf-8">
<title>Wexcombe Dance Company – A-Frame Sign</title>
<link rel="stylesheet" href="https://fonts.googleapis.com/css2?family=Poppins:wght@400;600;700&display=swap">
<style>
  :root {
    --stage-bg: #ececec;
    --navy-deep: #06123a;
    --navy: #0b2a6e;
    --blue: #1565c0;
    --blue-bright: #2f8fe0;
    --cyan: #5ccbe0;
    --green: #3ab54a;
    --white: #ffffff;
    --ink: #2b2b2b;
    --badge-purple: #6a2c80;
  }
  * { margin: 0; padding: 0; box-sizing: border-box; }
  html, body {
    width: 866px; height: 1200px; overflow: hidden;
    background: var(--stage-bg);
    font-family: "Poppins", sans-serif;
  }
  .sign {
    position: absolute; left: 33px; top: 0;
    width: 800px; height: 1200px;
    background: var(--white);
    overflow: hidden;
  }
  .hero-photo {
    position: absolute; left: 0; top: 0; width: 800px; height: 1000px;
    background:
      radial-gradient(ellipse 170px 420px at 640px 470px, rgba(120,180,255,0.55), rgba(60,120,220,0.15) 70%, transparent 100%),
      radial-gradient(ellipse 500px 260px at 600px 0px, rgba(70,160,240,0.7), transparent 80%),
      linear-gradient(180deg, #0f3a9a 0%, var(--navy) 30%, var(--navy-deep) 75%, #0a1a4a 100%);
  }
  .waves { position: absolute; left: 0; top: 0; width: 800px; height: 1200px; }
  .brand-name {
    position: absolute; left: 54px; top: 88px;
    color: var(--white);
    font-weight: 700; font-size: 60px; line-height: 63px;
    letter-spacing: -0.5px;
    text-transform: uppercase;
  }
  .styles-banner {
    position: absolute; left: 56px; top: 351px; width: 439px; height: 55px;
    background: var(--green);
    clip-path: polygon(12px 0, 100% 0, 96% 100%, 0 100%, 0 12px);
    color: var(--white);
    font-weight: 700; font-size: 32px; line-height: 55px;
    padding-left: 16px; letter-spacing: -0.5px;
  }
  .styles-list {
    position: absolute; left: 56px; top: 398px;
    list-style: none;
  }
  .styles-list li {
    color: var(--white);
    font-size: 42px; line-height: 59px; font-weight: 400;
    display: flex; align-items: center;
  }
  .styles-list li::before {
    content: ""; width: 12px; height: 12px; border-radius: 50%;
    background: var(--green);
    border: 3px solid var(--blue-bright);
    margin-right: 14px;
  }
  .therapy-note {
    position: absolute; left: 59px; top: 735px;
    color: var(--cyan); font-size: 22px; line-height: 30px;
  }
  .partner-badge {
    position: absolute; left: 323px; top: 709px;
    width: 152px; height: 152px; border-radius: 50%;
    background: var(--badge-purple);
    border: 6px solid var(--white);
  }
  .contact-email {
    position: absolute; left: 0; top: 1038px; width: 800px;
    text-align: center; color: var(--ink); font-size: 32px;
  }
  .call-pill {
    position: absolute; left: 142px; top: 1098px; width: 531px; height: 57px;
    background: var(--green); border-radius: 29px;
    color: var(--white); font-size: 42px; line-height: 57px;
    padding-left: 74px;
    box-shadow: 0 14px 14px -8px rgba(0,0,0,0.25);
  }
  .call-pill strong { font-weight: 700; }
  .call-icon {
    position: absolute; left: 4px; top: 1px; width: 55px; height: 55px;
    border-radius: 50%; background: var(--green);
    border: 3px solid var(--white);
    display: flex; align-items: center; justify-content: center;
  }
</style>
</head>
<body>
<main class="sign">
  <div class="hero-photo" role="img" aria-label="Photo of a dancer leaping on a blue-lit stage"></div>

  <svg class="waves" viewBox="0 0 844 1266" preserveAspectRatio="none" aria-hidden="true">
    <path d="M0,870 C250,1010 600,1010 844,880 L844,1266 L0,1266 Z" fill="#1565c0"/>
    <path d="M0,950 C150,1010 300,1050 420,1068 L0,1266 Z" fill="#5ccbe0"/>
    <path d="M0,985 C260,1110 600,1090 844,935 L844,1266 L0,1266 Z" fill="#2f8fe0"/>
    <path d="M0,1000 C280,1130 600,1100 844,955 L844,1266 L0,1266 Z" fill="#ffffff"/>
    <path d="M520,1008 C680,985 780,930 844,840 L844,868 C760,962 660,1000 520,1008 Z" fill="#3ab54a"/>
  </svg>

  <h1 class="brand-name">Wexcombe<br>Dance<br>Company</h1>

  <h2 class="styles-banner">OUR DANCE STYLE</h2>
  <ul class="styles-list">
    <li>HIP HOP</li>
    <li>BALLET</li>
    <li>CONTEMPORARY</li>
    <li>JAZZ &amp; CAPOEIRA</li>
  </ul>

  <p class="therapy-note">Creative Art Therapy -<br>QPHW Registered</p>
  <div class="partner-badge" role="img" aria-label="QPHW registration badge"></div>

  <p class="contact-email">info@wexcombedance.com</p>
  <p class="call-pill">
    <span class="call-icon">
      <svg width="28" height="28" viewBox="0 0 24 24" aria-hidden="true">
        <path fill="#fff" d="M6.6 10.8a15.1 15.1 0 0 0 6.6 6.6l2.2-2.2c.3-.3.7-.4 1-.2 1.1.4 2.3.6 3.6.6.6 0 1 .4 1 1V20c0 .6-.4 1-1 1A17 17 0 0 1 3 4c0-.6.4-1 1-1h3.5c.6 0 1 .4 1 1 0 1.3.2 2.5.6 3.6.1.3 0 .7-.2 1z"/>
      </svg>
    </span>
    Call <strong>1800 XX XXX</strong>
  </p>
</main>
</body>
</html>
```